Custom Truck shop New Business Card design

double sided business card including my new logo, brand colors and picking a font I attached, clean and modern look. I attached the old card for some reference. and would like to include the picture of the white truck attached. I would also like to have it with one of my employees info as well. (same info except name and title Brenna Dulwick Service Writer)

Todd Varnell
Owner

address
20418 E Pinecrest Service Rd S
STE 310
Larkspur Flats, MT 80517

phone 720-384-9172

email todd@ironcanyonrigs.com

website ironcanyonrogs.com

social @ironcanyonrigs

Target Market(s)

men 18-60

Industry/Entity Type

Automotive

Contact Information for Business Card

Todd Varnell Owner address 20418 E Pinecrest Service Rd S STE 310 Larkspur Flats, MT 80517 phone 720-384-9172 email todd@ironcanyonrigs.com website ironcanyonrogs.com social @ironcanyonrigs

Font styles to use
Other font styles liked:
• fonts attached

Requirements
Must have
• new logo, orange #FC68D, Charcoal #333333
Nice to have
• the white truck

```html
<!DOCTYPE html>
<html lang="en">
<head>
<meta charset="utf-8">
<title>Iron Canyon Rigs – Business Card</title>
<link href="https://fonts.googleapis.com/css2?family=Montserrat:wght@400;500;700;800&display=swap" rel="stylesheet">
<style>
  :root {
    --orange: #fc6d2d;
    --charcoal: #333333;
    --charcoal-deep: #262626;
    --panel: #1e1e1e;
    --white: #ffffff;
    --text-light: #e8e8e8;
    --backdrop: #bdbdbd;
  }
  * { box-sizing: border-box; margin: 0; padding: 0; }
  html, body { width: 1200px; height: 815px; overflow: hidden; }
  body {
    background: var(--backdrop);
    font-family: "Montserrat", Arial, sans-serif;
    display: flex;
    flex-direction: column;
    align-items: center;
    justify-content: center;
    gap: 20px;
  }
  .card {
    position: relative;
    width: 660px;
    height: 378px;
    border-radius: 22px;
    overflow: hidden;
    background: var(--charcoal);
    border-bottom: 5px solid var(--orange);
  }

  /* Front */
  .card-front__panel {
    position: absolute;
    top: 0; right: 0;
    width: 290px; height: 258px;
    background: linear-gradient(135deg, var(--charcoal-deep) 0%, var(--panel) 60%, var(--charcoal) 100%);
    border-left: 1px solid #5a5a5a;
  }
  .card-front__rule {
    position: absolute;
    left: 40px; right: 0; top: 258px;
    height: 1.5px;
    background: var(--orange);
  }
  .identity {
    position: absolute;
    left: 40px; top: 196px;
  }
  .identity__name {
    color: var(--orange);
    font-weight: 800;
    font-size: 30px;
    letter-spacing: 0.5px;
    text-transform: uppercase;
    line-height: 1;
  }
  .identity__title {
    color: var(--text-light);
    font-weight: 500;
    font-size: 15px;
    letter-spacing: 0.5px;
    margin-top: 6px;
    text-transform: uppercase;
  }
  .contacts {
    position: absolute;
    left: 40px; top: 276px;
    list-style: none;
    display: flex;
    flex-direction: column;
    gap: 7px;
  }
  .contacts__item {
    display: flex;
    align-items: center;
    gap: 10px;
    color: var(--text-light);
    font-size: 16px;
    font-weight: 500;
  }
  .contacts__icon { width: 14px; height: 14px; flex: none; }
  .address {
    position: absolute;
    right: 30px; top: 150px;
    text-align: right;
    color: var(--text-light);
    font-size: 15px;
    font-weight: 500;
    line-height: 1.55;
    font-style: normal;
  }
  .address__social {
    display: inline-flex;
    align-items: center;
    gap: 7px;
  }
  .address__dot {
    width: 12px; height: 12px;
    border-radius: 50%;
    background: var(--orange);
  }

  /* Back */
  .card-back__photo {
    position: absolute;
    inset: 0;
    background:
      linear-gradient(rgba(40,40,40,0.55), rgba(30,30,30,0.7)),
      radial-gradient(ellipse at 55% 55%, #9a9a9a 0%, #6b6b6b 35%, #3d3d3d 70%, #2a2a2a 100%);
  }
  .brand {
    position: absolute;
    left: 0; right: 0; top: 90px;
    display: flex;
    flex-direction: column;
    align-items: center;
    gap: 22px;
  }
  .brand__circle {
    width: 110px; height: 110px;
    border-radius: 50%;
    background: var(--white);
    border: 5px solid var(--orange);
  }
  .brand__name {
    color: var(--orange);
    font-weight: 800;
    font-size: 50px;
    letter-spacing: 1px;
    text-transform: uppercase;
    line-height: 1;
  }
</style>
</head>
<body>

  <section class="card card-front" aria-label="Business card front">
    <div class="card-front__panel"></div>
    <div class="card-front__rule"></div>

    <div class="identity">
      <h1 class="identity__name">Todd Varnell</h1>
      <p class="identity__title">Owner</p>
    </div>

    <address class="address">
      20418 E Pinecrest Service Rd S STE 310<br>
      Larkspur Flats, MT 80517<br>
      <span class="address__social"><span class="address__dot"></span>@ironcanyonrigs</span>
    </address>

    <ul class="contacts">
      <li class="contacts__item">
        <svg class="contacts__icon" viewBox="0 0 24 24" aria-hidden="true"><path fill="#fc6d2d" d="M6.6 10.8a15.2 15.2 0 0 0 6.6 6.6l2.2-2.2a1 1 0 0 1 1-.25 11.4 11.4 0 0 0 3.6.57 1 1 0 0 1 1 1V20a1 1 0 0 1-1 1A17 17 0 0 1 3 4a1 1 0 0 1 1-1h3.5a1 1 0 0 1 1 1c0 1.250.2 2.450.57 3.570a1 1 0 0 1-.25 1z"/></svg>
        555-384-9172
      </li>
      <li class="contacts__item">
        <svg class="contacts__icon" viewBox="0 0 24 24" aria-hidden="true"><rect x="2" y="5" width="20" height="14" rx="2" fill="#fc6d2d"/><path d="M3 6l9 7 9-7" fill="none" stroke="#333" stroke-width="2"/></svg>
        todd@ironcanyonrigs.com
      </li>
      <li class="contacts__item">
        <svg class="contacts__icon" viewBox="0 0 24 24" aria-hidden="true"><circle cx="12" cy="12" r="10" fill="#fc6d2d"/><path d="M2 12h20M12 2c3 3 3 17 0 20M12 2c-3 3-3 17 0 20" fill="none" stroke="#333" stroke-width="1.5"/></svg>
        www.ironcanyonrogs.com
      </li>
    </ul>
  </section>

  <section class="card card-back" aria-label="Business card back">
    <div class="card-back__photo" role="img" aria-label="Photo of a lifted white pickup truck parked in a snowy lot"></div>
    <div class="brand">
      <div class="brand__circle"></div>
      <p class="brand__name">Iron Canyon Rigs</p>
    </div>
  </section>

</body>
</html>
```